Cobalt Landscaping Landing Page

I require a landing page for my landscaping business.

My business plan revolves around hooking clients with weeding services. Not lawn herbicide sprays, but actual hand weeding and bed maintenance. I've found my niche as most people do not want to do this kind of work. From there I often upsell clients into actual hardscaping or softscaping.

I like things to be clean, concise, and to the point. Not overly flashy, but not so minimal that that it's boring. My logo is a very good example of what I like.

The business is LGBTQ owned and operated. I do not broadcast this but I feel the logo itself, along with the name is usually enough to tip people into assumption. I'm not opposed to color, but I do not want the page to scream "gay". My favourite color is yellow...

I used to be a door to door salesman so I'm doing something different where I want to do all my selling in my first meeting with the client. With this said I do not need a section for "work pictures", as I have photos of my work on my tablet, which I show the client during the consultation.

Ideally i'd like my web site to actually be just a landing page. I'd like room for all the following information within the page;

- description of services;
Weeding of Perennial and Flower Beds
Selective Pruning of Trees and Shrubs
Hedging
Landscape Construction
Landscape Design
Total Lawn Treatment Plans
Landscape Pest Control

- contact information, phone, email
Gerald Ostrunek
204-571-3342
ger.ostrunek@maplethorn.com

- "free estimates" somewhere on the page that is either led to by the eye, or very easy to notice and see

- and my slogan which is "dependable, reliable, consistent"

- room for a link to my future revuly account so they can see reviews from real people

- My Logo present

Any or all of these can be custom made graphics or simply text, whatever looks best

I do not want people to have to search for information throughout. Design it in such a way that either the eye flows naturally from one piece of information to the other, or that it's all compartmentalized neatly enough that everything is easy to find.

As I am a landscape and outdoor maintenance service I'm no opposed to images such as flowers, trees, landscaping, etc being present. However please note that my main focus and source of income comes from weeding services, everything else is bonus cash.

Many of my clients are extremely wealthy individuals who pay over $1000 for the season for me just to show up and pull weeds. So making the website appeal to wealthy people as opposed to the average joe is paramount.

I do not cut grass. Please do not have any indication on the website, either through writing or graphics that implies that I cut grass. There are enough companies doing that.

Target Market(s)

Wealthy, often elderly individuals.

Industry/Entity Type

Landscape Gardening

Coding

Coded - Design and coding required

Number of Pages Required

1 page

Font styles to use
Sans Serif

Colors

Designer to choose colors to be used in the design.

Requirements
Must have
• - description of services;
• Weeding of Perennial and Flower Beds
• Selective Pruning of Trees and Shrubs
• Hedging
• Landscape Construction
• Landscape Design
• Total Lawn Treatment Plans
• Landscape Pest Control
• - contact information, phone, email
• Gerald Ostrunek
• 204-571-3342
• ger.ostrunek@maplethorn.com
• - "free estimates" somewhere on the page that is either led to by the eye, or very easy to notice and see
• - and my slogan which is "dependable, reliable, consistent"
• - room for a link to my future revuly account so they can see reviews from real people
• - My Logo present
Nice to have
• Flowers or weeds depicted. Possibly some hardscaping and softscaping if it doesnt look too bulky and crowded.
Should not have
• grass

```html
<!DOCTYPE html>
<html lang="en">
<head>
<meta charset="utf-8">
<title>Cobalt Landscaping</title>
<link rel="stylesheet" href="https://fonts.googleapis.com/css2?family=Montserrat:wght@400;500;700&display=swap">
<style>
  :root {
    --ink: #1c1c1c;
    --body: #444444;
    --muted: #b3b3b3;
    --faint: #ececec;
    --rule: #efefef;
    --icon: #6f6f6f;
    --icon-soft: #d2d2d2;
    --accent: #e2392c;
    --brand-dot: #e8b923;
    --paper: #ffffff;
    --leaf-dark: #3e5a2c;
    --leaf: #7c9a4a;
    --stone: #c9b79c;
    --maple: #9a4a3c;
  }
  * { box-sizing: border-box; margin: 0; padding: 0; }
  html, body { width: 1200px; height: 800px; overflow: hidden; background: var(--paper); }
  body { font-family: "Montserrat", Arial, sans-serif; color: var(--ink); position: relative; }

  .hero-photo {
    position: absolute; left: 0; top: 0; width: 484px; height: 800px;
    background:
      radial-gradient(ellipse at 55% 22%, var(--maple) 0%, rgba(154,74,60,0) 38%),
      radial-gradient(ellipse at 75% 85%, var(--stone) 0%, rgba(201,183,156,0) 55%),
      linear-gradient(180deg, #d9e3d0 0%, var(--leaf) 28%, var(--leaf-dark) 48%, var(--leaf) 58%, var(--stone) 78%, #bfae92 100%);
  }

  .content { position: absolute; left: 555px; top: 0; width: 540px; height: 800px; }

  .brand { position: absolute; top: 55px; left: 0; display: flex; align-items: center; gap: 8px; }
  .brand-dot { width: 14px; height: 14px; border-radius: 50%; background: var(--brand-dot); }
  .brand-name { font-size: 22px; font-weight: 500; letter-spacing: -0.4px; text-transform: uppercase; color: var(--ink); line-height: 26px; }
  .slogan { position: absolute; top: 82px; left: 1px; font-size: 20.8px; font-weight: 700; color: var(--faint); text-transform: uppercase; letter-spacing: 0.2px; line-height: 26px; }

  .estimate { position: absolute; top: 196px; left: 1px; }
  .estimate-label { font-size: 11px; font-weight: 700; letter-spacing: 1.6px; text-transform: uppercase; color: var(--accent); margin-bottom: 10px; }
  .estimate-contact { font-style: normal; font-size: 14px; line-height: 22px; color: var(--body); letter-spacing: 0.2px; }
  .estimate-contact .contact-name { color: var(--ink); font-weight: 500; }

  .services { position: absolute; top: 384px; left: 0; list-style: none; }
  .services li { font-size: 19px; line-height: 30.2px; color: var(--muted); letter-spacing: 0.4px; }
  .services li.is-active .service-name { color: var(--ink); }

  .copyright { position: absolute; top: 743px; left: 1px; font-size: 10.5px; color: var(--body); letter-spacing: 0.2px; }

  .review-button {
    position: absolute; top: 730px; left: 356px; width: 161px; height: 35px;
    background: var(--accent); border-radius: 2px; color: #fff; text-decoration: none;
    display: flex; align-items: center; justify-content: center; gap: 8px;
    font-size: 10.5px; font-weight: 700; letter-spacing: 0.1px;
  }
  .review-button .mark { width: 12px; height: 12px; border-radius: 50%; background: #fff; }

  .side-rail { position: absolute; left: 1124px; top: 0; width: 76px; height: 800px; border-left: 1px solid var(--rule); }
  .rail-icon { position: absolute; left: 24px; width: 18px; height: 18px; display: block; }
</style>
</head>
<body>
  <div class="hero-photo" role="img" aria-label="Photograph of a landscaped courtyard with a red maple, clipped hedges, stone walls, built-in bench and a round planter on a brick path"></div>

  <main class="content">
    <header>
      <div class="brand"><span class="brand-dot"></span><span class="brand-name">Cobalt Landscaping</span></div>
      <p class="slogan">Dependable, Reliable, Consistent</p>
    </header>

    <section class="estimate">
      <p class="estimate-label">Free Estimates</p>
      <address class="estimate-contact">
        <span class="contact-name">Gerald Ostrunek</span><br>
        204-571-3342<br>
        ger.ostrunek@maplethorn.com
      </address>
    </section>

    <ol class="services">
      <li>01. <span class="service-name">Hedging</span></li>
      <li>02. <span class="service-name">Landscape Construction</span></li>
      <li class="is-active">03. <span class="service-name">Landscape Design</span></li>
      <li>04. <span class="service-name">Landscape Pest Control</span></li>
      <li>05. <span class="service-name">Selective Pruning of Trees &amp; Shrubs</span></li>
      <li>06. <span class="service-name">Total Lawn Treatment Plans</span></li>
      <li>07. <span class="service-name">Weeding of Perennial &amp; Flower Beds</span></li>
    </ol>

    <footer>
      <p class="copyright">© 2017 Cobalt Landscaping Inc.</p>
      <a class="review-button" href="#"><span class="mark"></span>REVIEW US ON REVULY</a>
    </footer>
  </main>

  <aside class="side-rail">
    <svg class="rail-icon" style="top:57px" viewBox="0 0 18 18" aria-label="About">
      <circle cx="9" cy="9" r="8" fill="var(--icon)"/>
      <rect x="8" y="8" width="2" height="5.5" fill="#fff"/>
      <circle cx="9" cy="5.5" r="1.1" fill="#fff"/>
    </svg>
    <svg class="rail-icon" style="top:91px" viewBox="0 0 18 18" aria-label="Contact">
      <rect x="1" y="3" width="16" height="12" rx="1.5" fill="var(--icon)"/>
      <path d="M2.5 5 L9 9.5 L15.5 5" fill="none" stroke="#fff" stroke-width="1.4"/>
    </svg>
    <svg class="rail-icon" style="top:676px" viewBox="0 0 18 18" aria-label="Social link">
      <circle cx="9" cy="9" r="5" fill="var(--icon-soft)"/>
    </svg>
    <svg class="rail-icon" style="top:710px" viewBox="0 0 18 18" aria-label="Social link">
      <circle cx="9" cy="9" r="5" fill="var(--icon-soft)"/>
    </svg>
    <svg class="rail-icon" style="top:744px" viewBox="0 0 18 18" aria-label="Favourite">
      <path d="M9 15.5 L2.6 9.2 C0.8 7.4 1.6 3.5 4.8 3.3 C6.6 3.2 8.2 4.4 9 5.8 C9.8 4.4 11.4 3.2 13.2 3.3 C16.4 3.5 17.2 7.4 15.4 9.2 Z" fill="var(--icon-soft)"/>
    </svg>
  </aside>
</body>
</html>
```